Window Cleaning Flyer targeting Shopfronts and Small Commercial Work

Single page flyer similar to the flyer targeting small commercial work and shopfronts

Please include the following text:

Brisk Pane Services delivers high quality service to suburbs all around Melbourne. From Frankston to Kalkallo, Brisk has you covered!

With over 10 years experience, Brisk specialises in providing:
- Window Cleaning: via elevated work platforms, rope access and extension poles
- Pressure Cleaning: Including chlorine treatment to prevent mould regrowth on concrete area
- Roof Gutter Cleaning: using our ladder free gutter vacuum

We pride ourselves on neat and professional presentation and vast geographical reach across Melbourne.

Our services can be completed on a frequency that meets your window cleaning needs. Whether a weekly clean or a yearly service.

Brisk Pane Services Melbourne takes care of all your window cleaning needs.

Contact Us now for free quote!

Target Market(s)

Small business and commercial building owners

Industry/Entity Type

Window Cleaning

Requirements
Must have
• Only use photos/logos provided
Should not have
• Stock phots

```html
<!DOCTYPE html>
<html lang="en">
<head>
<meta charset="utf-8">
<title>Brisk Pane Services – Flyer</title>
<link href="https://fonts.googleapis.com/css2?family=Exo+2:wght@400;700;800&family=Roboto+Condensed:wght@300;400&display=swap" rel="stylesheet">
<style>
  :root {
    --page-bg: #e9e9e9;
    --paper: #f5f6f6;
    --brand-blue: #0d5389;
    --accent-blue: #1a72b8;
    --heading-blue: #1a6fb5;
    --charcoal: #3a3a3a;
    --band-dark: #444444;
    --yellow: #f6ec1b;
    --ink: #1f1f1f;
    --white: #ffffff;
  }
  * { margin: 0; padding: 0; box-sizing: border-box; }
  html, body { width: 1200px; height: 1200px; overflow: hidden; background: var(--page-bg); }
  .flyer {
    position: absolute; left: 191px; top: 20px;
    width: 916px; height: 1298px;
    transform: scale(0.8937); transform-origin: top left;
    background: var(--paper);
    overflow: hidden;
    box-shadow: 0 6px 18px rgba(0,0,0,.25);
    font-family: "Exo 2", sans-serif;
  }
  .flyer-shapes { position: absolute; inset: 0; }
  .brand-name {
    position: absolute; top: 110px; left: 0; width: 100%;
    text-align: center; color: var(--yellow);
    font-family: "Exo 2", sans-serif; font-weight: 800; font-size: 64px; letter-spacing: 1px;
  }
  .tagline {
    position: absolute; top: 228px; left: 0; width: 100%;
    text-align: center; color: var(--yellow);
    font-size: 25px; line-height: 32px; letter-spacing: .5px;
  }
  .photo-frame {
    position: absolute; width: 290px; height: 290px; border-radius: 50%;
    background: var(--white); box-shadow: 0 6px 10px rgba(0,0,0,.25);
    display: flex; align-items: center; justify-content: center;
  }
  .photo-frame .photo { width: 250px; height: 250px; border-radius: 50%; }
  .photo-left { left: 1px; top: 338px; }
  .photo-left .photo { background: linear-gradient(135deg, #3b3f44 0%, #c99a66 45%, #8a6a45 70%, #d9d4cc 100%); }
  .photo-right { left: 628px; top: 328px; }
  .photo-right .photo { background: linear-gradient(135deg, #6b3a2c 0%, #2b2b2b 45%, #d0602a 65%, #7aa255 100%); }
  .quote-badge {
    position: absolute; left: 316px; top: 441px; width: 284px; height: 284px; border-radius: 50%;
    background: var(--white); box-shadow: 0 6px 10px rgba(0,0,0,.25);
    display: flex; align-items: center; justify-content: center;
  }
  .quote-badge .quote-inner {
    width: 244px; height: 244px; border-radius: 50%; background: var(--accent-blue);
    display: flex; align-items: center; justify-content: center; text-align: center;
    color: var(--yellow); font-weight: 800; font-size: 31px; line-height: 38px; letter-spacing: 1px;
  }
  .services {
    position: absolute; left: 115px; top: 752px; width: 700px; color: var(--ink);
  }
  .services h2 {
    color: var(--heading-blue); font-size: 21px; font-weight: 800; letter-spacing: .6px; margin-bottom: 12px;
  }
  .services ul { list-style: none; }
  .services li {
    position: relative; padding-left: 26px; font-size: 20.5px; line-height: 26px;
    letter-spacing: .8px; margin-bottom: 11px;
  }
  .services li::before { content: "•"; position: absolute; left: 0; top: 0; }
  .highlight-pill {
    position: absolute; left: 131px; width: 654px; height: 63px; border-radius: 30px;
    background: var(--accent-blue); color: var(--white);
    display: flex; align-items: center; justify-content: center; text-align: center;
    font-family: "Roboto Condensed", sans-serif; font-weight: 300; font-size: 20px; line-height: 26px;
    padding: 0 40px;
  }
  .pill-1 { top: 957px; }
  .pill-2 { top: 1029px; }
  .pill-3 { top: 1101px; }
  .contact-line {
    position: absolute; left: 0; width: 820px; top: 1222px; text-align: center;
    color: var(--white); font-family: "Roboto Condensed", sans-serif; font-weight: 400; font-size: 64px;
  }
</style>
</head>
<body>
  <div class="flyer">
    <svg class="flyer-shapes" width="916" height="1298" viewBox="0 0 916 1298">
      <path d="M0 0 H916 V400 Q470 625 0 320 Z" fill="var(--charcoal)"/>
      <path d="M0 0 H916 V378 Q470 585 0 300 Z" fill="var(--brand-blue)"/>
      <path d="M0 1240 Q458 1120 916 1240 V1298 H0 Z" fill="var(--band-dark)"/>
      <path d="M0 1250 Q458 1135 916 1250 V1298 H0 Z" fill="var(--charcoal)"/>
    </svg>

    <div class="brand-name">Brisk Pane Services</div>
    <p class="tagline">We are delivers high quality service to<br>suburbs all around Melbourne. From<br>Frankston to Kalkallo, Brisk has you covered!</p>

    <div class="photo-frame photo-left"><div class="photo" role="img" aria-label="Photo of a technician cleaning high facade windows with an extension pole"></div></div>
    <div class="photo-frame photo-right"><div class="photo" role="img" aria-label="Photo of a crew on an elevated work platform cleaning a brick building"></div></div>

    <div class="quote-badge"><div class="quote-inner">Contact<br>Us now for<br>free quote!</div></div>

    <section class="services">
      <h2>With over 10 years experience, Brisk specialises in providing:</h2>
      <ul>
        <li>Window Cleaning: via elevated work platforms, rope access and extension poles</li>
        <li>Pressure Cleaning: Including chlorine treatment to prevent mould regrowth on concrete area</li>
        <li>Roof Gutter Cleaning: using our ladder free gutter vacuum</li>
      </ul>
    </section>

    <div class="highlight-pill pill-1">We pride ourselves on neat and professional presentation and vast geographical reach across Melbourne.</div>
    <div class="highlight-pill pill-2">Our services can be completed on a frequency that meets your window cleaning needs. Whether a weekly clean or a yearly service.</div>
    <div class="highlight-pill pill-3">Brisk Pane Services Melbourne takes care of all your window cleaning needs.</div>

    <div class="contact-line">your contact info here</div>
  </div>
</body>
</html>
```